Postcard flyers for text vouchers

Postcard flyer to drive people to text for local vouchers delivered straight to their mobile, alternatively they can check out the websites.
Double sided, full colour A6 size. 105mm x 148.5mm http://www.brindleprint.example/artwork-guide.html
Postcard will be available in high footfall areas must be eye catching and compelling, but keep message simple. Wording as attached, side one headline grabbing, side two in style of a tag cloud giving a flavour of vouchers/savings available in their local area.
Updates

Project Deadline Extended
Reason: Research has shown wider area for website required therefore by county [Hollowmere Vouchers] rather than smaller regions. Focus on entertainment and shopping for flyer.

Target Market(s)

Target 18-55 year olds
Core 25-45???
male and female

Requirements
Must have
• Stand out

```html
<!DOCTYPE html>
<html lang="en">
<head>
<meta charset="utf-8">
<title>Vouchers – How Much Can You Save</title>
<link rel="stylesheet" href="https://fonts.googleapis.com/css2?family=Arimo:ital,wght@0,400;0,700;1,400;1,700&family=Cinzel:wght@400;500&family=Gentium+Book+Plus:wght@400;700&display=swap">
<style>
  :root {
    --sun: #ffff00;
    --sky: #0000ff;
    --ink: #000000;
    --paper: #ffffff;
    --signal: #ff0000;
    --highlight: #ffff33;
  }
  html, body { margin: 0; padding: 0; overflow: hidden; background: var(--paper); }
  .flyer { display: block; width: 851px; height: 1200px; }
  .headline { font-family: "Arimo", Arial, sans-serif; font-weight: 700; font-style: italic; fill: var(--ink); }
  .banner-word { font-family: "Arimo", Arial, sans-serif; font-weight: 700; fill: var(--paper); }
  .tagline { font-family: "Arimo", Arial, sans-serif; font-style: italic; fill: var(--highlight); }
  .offer-list { font-family: "Gentium Book Plus", Georgia, serif; fill: var(--paper); font-size: 30px; }
  .deal-big { font-family: "Cinzel", Georgia, serif; fill: var(--paper); }
  .deal-small { font-family: "Arimo", Arial, sans-serif; fill: var(--paper); }
  .question-mark { font-family: "Gentium Book Plus", Georgia, serif; font-weight: 700; fill: var(--ink); }
</style>
</head>
<body>
<svg class="flyer" viewBox="0 0 851 1200" xmlns="http://www.w3.org/2000/svg" role="img" aria-label="Vouchers flyer: how much can you save">
  <defs>
    <radialGradient id="sky-glow" cx="330" cy="520" r="380" gradientUnits="userSpaceOnUse">
      <stop offset="0" stop-color="#ffffff"/>
      <stop offset="0.3" stop-color="#ffffff"/>
      <stop offset="0.75" stop-color="#0000ff"/>
      <stop offset="1" stop-color="#0000ff"/>
    </radialGradient>
    <radialGradient id="sun-glow" cx="640" cy="240" r="330" gradientUnits="userSpaceOnUse">
      <stop offset="0" stop-color="#ffffff"/>
      <stop offset="0.6" stop-color="#ffff00"/>
      <stop offset="1" stop-color="#ffff00"/>
    </radialGradient>
  </defs>

  <rect class="band-top" x="0" y="0" width="851" height="375" fill="url(#sun-glow)"/>
  <rect class="band-bottom" x="0" y="375" width="851" height="825" fill="url(#sky-glow)"/>

  <text class="question-mark" x="125" y="262" font-size="250" text-anchor="middle">?</text>

  <text class="headline" x="213" y="106" font-size="36" textLength="372" lengthAdjust="spacingAndGlyphs">How Much Can You</text>
  <rect x="213" y="110" width="380" height="3" fill="var(--ink)"/>
  <text class="headline" x="218" y="196" font-size="66" textLength="156" lengthAdjust="spacingAndGlyphs">Save</text>
  <rect x="216" y="201" width="162" height="4" fill="var(--ink)"/>

  <g class="voucher-banner" transform="translate(420 437) rotate(-33.8)">
    <rect x="-393" y="-118" width="786" height="236" fill="var(--signal)"/>
    <rect x="-381" y="-106" width="762" height="212" fill="none" stroke="var(--paper)" stroke-width="9" stroke-dasharray="0 17.3" stroke-linecap="round"/>
    <text class="banner-word" x="0" y="70" font-size="200" text-anchor="middle" textLength="700" lengthAdjust="spacingAndGlyphs">Vouchers</text>
  </g>

  <g class="tagline-group">
    <g transform="translate(277 734) rotate(-33.8)">
      <text class="tagline" x="0" y="0" font-size="40" textLength="520" lengthAdjust="spacingAndGlyphs">Save money when you</text>
      <rect x="0" y="5" width="530" height="3" fill="var(--highlight)"/>
    </g>
    <g transform="translate(309 793) rotate(-33.8)">
      <text class="tagline" x="0" y="0" font-size="40" textLength="270" lengthAdjust="spacingAndGlyphs">shop locally</text>
      <rect x="0" y="5" width="276" height="3" fill="var(--highlight)"/>
    </g>
  </g>

  <g class="exclamation" fill="var(--paper)">
    <path d="M721 540 Q752 505 783 540 L761 770 Q752 785 743 770 Z"/>
    <circle cx="751" cy="846" r="40"/>
  </g>

  <g class="offer-list">
    <circle cx="44" cy="904" r="5" fill="var(--paper)"/><text x="64" y="913" textLength="191">Entertainment</text>
    <circle cx="44" cy="938" r="5" fill="var(--paper)"/><text x="64" y="947" textLength="284">Free Entry for Events</text>
    <circle cx="44" cy="973" r="5" fill="var(--paper)"/><text x="64" y="982" textLength="183">Theatre Deals</text>
    <circle cx="44" cy="1007" r="5" fill="var(--paper)"/><text x="64" y="1016" textLength="264" xml:space="preserve">Furniture  vouchers</text>
    <circle cx="44" cy="1042" r="5" fill="var(--paper)"/><text x="64" y="1051" textLength="186">Fashion Deals</text>
    <circle cx="44" cy="1076" r="5" fill="var(--paper)"/><text x="64" y="1085" textLength="215">Insurance offers</text>
    <circle cx="44" cy="1111" r="5" fill="var(--paper)"/><text x="64" y="1120" textLength="495">FREE sessions solicitors/accountants</text>
    <circle cx="44" cy="1145" r="5" fill="var(--paper)"/><text x="64" y="1154" textLength="679">building/plumbing/home services huge discounts</text>
  </g>

  <g class="deals">
    <text class="deal-big" x="458" y="942" font-size="66" textLength="223" lengthAdjust="spacingAndGlyphs">2 <tspan font-size="50">FOR</tspan> 1</text>
    <text class="deal-big" x="511" y="1021" font-size="66" textLength="151" lengthAdjust="spacingAndGlyphs">50%</text>
    <text class="deal-small" x="513" y="1064" font-size="32" textLength="160" lengthAdjust="spacingAndGlyphs">Eating out</text>
  </g>
</svg>
</body>
</html>
```